KELVARA Branded Wellness Pouch Design for Clinical Study Kit

Overview:
We are creating custom zippered pouches for our “KELVARA Study Fuel Kits,” which will be distributed to physicians, nurses, and research coordinators participating in a national clinical study. We need a clean, professional design for the front of the pouch that incorporates our existing KELVARA logo and the new supporting text.
Design Requirements:
Keep the existing KELVARA logo intact (we’ll upload the file).
Add the text “Study Fuel Kit” immediately following the logo, using the same or a complementary font.
Add a tagline below that reads:
Power up. Kelvara. Go again.
Use a layout that looks balanced, legible, and polished when printed on a small pouch.
Stay consistent with our brand color palette (blue from the logo)
The overall style should feel modern, wellness-driven, and professional — think premium, science-forward, and sleek.
Audience:
This kit will be given to medical professionals, so the design should feel elevated and credible (not flashy or overly playful).
Deliverables:
Vector file (AI, EPS)
It is a frosted white, zippered vinyl pouch (9 1/2 " x 8 1/4 " x 2 1/2 ")
The imprint size is (6 3/4" W x 4 1/2" H)
The imprint can only be 1-color, so in this case - we would like the color to be the dark blue (#06173c)

```html
<!DOCTYPE html>
<html lang="en">
<head>
<meta charset="utf-8">
<title>KELVARA Study Fuel Kit – Pouch Front</title>
<link rel="stylesheet" href="https://fonts.googleapis.com/css2?family=Jost:wght@400;600;700&display=swap">
<style>
  :root {
    --ink: #06173c;
    --page: #ffffff;
    --pouch: #eeeff1;
    --hex-light: #dfe1e5;
    --hex-mid: #c3c7ce;
  }
  * { margin: 0; padding: 0; box-sizing: border-box; }
  html, body {
    width: 1200px;
    height: 3000px;
    overflow: hidden;
    background: var(--page);
  }
  .canvas {
    position: relative;
    width: 1200px;
    height: 3000px;
    display: flex;
    align-items: center;
    justify-content: center;
  }
  .pouch-front {
    position: relative;
    width: 1000px;
    height: 780px;
    border-radius: 22px;
    background: linear-gradient(160deg, #f4f5f6 0%, var(--pouch) 55%, #e6e8ea 100%);
    overflow: hidden;
    color: var(--ink);
    font-family: "Jost", "Futura", sans-serif;
  }
  .hex-field {
    position: absolute;
  }
  .hex-field--top {
    top: 0;
    right: 0;
    width: 560px;
    height: 300px;
    background: radial-gradient(ellipse at 85% 25%, var(--hex-mid) 0%, var(--hex-light) 40%, rgba(238,239,241,0) 75%);
  }
  .hex-field--bottom {
    bottom: 0;
    left: 0;
    width: 620px;
    height: 230px;
    background: radial-gradient(ellipse at 20% 90%, var(--hex-mid) 0%, var(--hex-light) 40%, rgba(238,239,241,0) 75%);
  }
  .imprint {
    position: absolute;
    left: 0;
    right: 0;
    top: 200px;
    display: flex;
    flex-direction: column;
    align-items: center;
  }
  .brand {
    display: flex;
    flex-direction: column;
    align-items: flex-end;
  }
  .brand-row {
    display: flex;
    align-items: center;
    gap: 18px;
  }
  .brand-mark {
    width: 46px;
    height: 46px;
    background: var(--ink);
  }
  .brand-name {
    font-weight: 600;
    font-size: 96px;
    line-height: 1;
    letter-spacing: -2px;
    transform: scaleX(0.72);
    transform-origin: left center;
    margin-right: -150px;
  }
  .brand-study {
    font-weight: 600;
    font-size: 15px;
    margin-top: 6px;
    letter-spacing: 0.1px;
  }
  .kit-title {
    margin-top: 70px;
    font-weight: 700;
    font-size: 108px;
    line-height: 1;
    letter-spacing: -3px;
    transform: scaleX(0.86);
  }
  .kit-tagline {
    margin-top: 16px;
    font-weight: 400;
    font-size: 42px;
    letter-spacing: 1px;
  }
</style>
</head>
<body>
  <main class="canvas">
    <section class="pouch-front">
      <div class="hex-field hex-field--top" role="img" aria-label="Faint grey hexagon molecular pattern"></div>
      <div class="hex-field hex-field--bottom" role="img" aria-label="Faint grey hexagon molecular pattern"></div>

      <div class="imprint">
        <div class="brand">
          <div class="brand-row">
            <span class="brand-mark"></span>
            <span class="brand-name">KELVARA U.S.</span>
          </div>
          <p class="brand-study">Novex Disc Randomized, Sham-Controlled, Multi-Center, Double Blind Clinical Trial</p>
        </div>
        <h1 class="kit-title">STUDY FUEL KIT</h1>
        <p class="kit-tagline">Power up. Kelvara. Go again.</p>
      </div>
    </section>
  </main>
</body>
</html>
```